Business Card Design Project

We need a creative business card idea. For social media app.

www.pebblenote.example

Requirements
Must have
• Shaped like an Zentra. download and sign in on our Pebblenote app (free) and use similar design as in "Me" section but with new attached logo.

Everything on sample card file plus twitter : @PebbleNoteApp
facebook leg /PebbleNote

```html
<!DOCTYPE html>
<html lang="en">
<head>
<meta charset="utf-8">
<title>Pebblenote business card</title>
<link href="https://fonts.googleapis.com/css2?family=Open+Sans:ital,wght@0,400;0,600;0,700;1,400&display=swap" rel="stylesheet">
<style>
  :root {
    --page-bg: #e6e8eb;
    --card-white: #ffffff;
    --strip-black: #1c1c1e;
    --strip-text: #d7dadd;
    --sky-pale: #dcf0fb;
    --sky-blue: #2aa8e0;
    --ink-grey: #555a60;
    --ink-soft: #8a9096;
    --icon-blue: #2aa8e0;
  }
  * { box-sizing: border-box; margin: 0; padding: 0; }
  html, body { width: 1200px; height: 750px; overflow: hidden; }
  body {
    background: var(--page-bg);
    font-family: "Open Sans", Arial, sans-serif;
    position: relative;
  }
  .card {
    position: absolute;
    top: 220px;
    width: 500px;
    height: 310px;
    background: var(--card-white);
    overflow: hidden;
    box-shadow: 0 6px 18px rgba(0,0,0,.18);
  }
  .card--front { left: 70px; }
  .card--back { left: 630px; }

  /* front */
  .social-strip {
    position: absolute; left: 0; top: 0; bottom: 0; width: 58px;
    background: var(--strip-black);
    display: flex; flex-direction: column; align-items: center; justify-content: space-evenly;
    list-style: none;
  }
  .social-item {
    display: flex; flex-direction: column-reverse; align-items: center; gap: 10px;
  }
  .social-dot { width: 14px; height: 14px; border-radius: 50%; background: var(--sky-blue); flex: none; }
  .social-handle {
    writing-mode: vertical-rl; transform: rotate(180deg);
    color: var(--strip-text); font-size: 11px; font-style: italic; letter-spacing: .3px;
    white-space: nowrap;
  }
  .cloud-band { position: absolute; left: 58px; top: 0; width: 442px; height: 150px; }
  .brand-name {
    position: absolute; right: 26px; top: 20px;
    font-weight: 700; font-size: 34px; color: var(--sky-blue); letter-spacing: -.5px;
  }
  .person { position: absolute; left: 210px; top: 82px; text-align: right; width: 200px; }
  .person__name { font-weight: 700; font-size: 20px; color: var(--ink-grey); }
  .person__role { font-style: italic; font-size: 15px; color: var(--ink-soft); }
  .contacts { position: absolute; left: 82px; top: 168px; list-style: none; }
  .contacts li {
    display: flex; align-items: center; gap: 16px;
    font-weight: 600; font-size: 15px; color: var(--ink-grey); height: 38px;
  }
  .contacts svg { width: 22px; height: 22px; flex: none; }

  /* back */
  .pattern-band { position: absolute; left: 0; top: 0; width: 500px; height: 90px; }
  .back-brand {
    position: absolute; left: 0; right: 0; top: 150px; text-align: center;
    font-weight: 700; font-size: 44px; color: var(--sky-blue); letter-spacing: -.5px;
  }
</style>
</head>
<body>

<section class="card card--front" aria-label="Business card front">
  <svg class="cloud-band" viewBox="0 0 442 150" preserveAspectRatio="none" aria-hidden="true">
    <path fill="var(--sky-pale)" d="M0 0H442V118Q420 140 398 124Q376 146 350 128Q326 148 300 130Q276 150 250 132Q226 150 200 134Q176 150 150 136Q126 152 100 138Q76 154 50 140Q26 154 0 142Z"/>
  </svg>
  <div class="brand-name">Pebblenote</div>

  <div class="person">
    <p class="person__name">Tomas Reyes</p>
    <p class="person__role">co-founder</p>
  </div>

  <ul class="contacts">
    <li>
      <svg viewBox="0 0 24 24" aria-hidden="true"><rect x="2" y="5" width="20" height="14" rx="1.5" fill="none" stroke="var(--icon-blue)" stroke-width="2"/><path d="M3 6l9 7 9-7" fill="none" stroke="var(--icon-blue)" stroke-width="2"/></svg>
      tomas.reyes@pebblenote.example
    </li>
    <li>
      <svg viewBox="0 0 24 24" aria-hidden="true"><rect x="6" y="2" width="12" height="20" rx="2.5" fill="var(--icon-blue)"/><rect x="8" y="5" width="8" height="12" fill="#fff"/></svg>
      555.014.2278
    </li>
    <li>
      <svg viewBox="0 0 24 24" aria-hidden="true"><circle cx="12" cy="12" r="9.5" fill="none" stroke="var(--icon-blue)" stroke-width="2"/><ellipse cx="12" cy="12" rx="4" ry="9.5" fill="none" stroke="var(--icon-blue)" stroke-width="1.6"/><path d="M2.5 12h19M4.5 7h15M4.5 17h15" stroke="var(--icon-blue)" stroke-width="1.4"/></svg>
      www.pebblenote.example
    </li>
  </ul>

  <ul class="social-strip" aria-label="Social profiles">
    <li class="social-item">
      <span class="social-dot" aria-hidden="true"></span>
      <span class="social-handle">@PebbleNoteApp</span>
    </li>
    <li class="social-item">
      <span class="social-dot" aria-hidden="true"></span>
      <span class="social-handle">/PebbleNote</span>
    </li>
  </ul>
</section>

<section class="card card--back" aria-label="Business card back">
  <svg class="pattern-band" viewBox="0 0 500 90" preserveAspectRatio="none" role="img" aria-label="Blue cloud band with a faint pattern of small app icons">
    <path fill="var(--sky-blue)" d="M0 0H500V62Q475 86 450 66Q425 90 400 68Q375 92 350 70Q325 92 300 70Q275 92 250 70Q225 92 200 70Q175 92 150 68Q125 90 100 66Q75 88 50 64Q25 86 0 62Z"/>
  </svg>
  <div class="back-brand">Pebblenote</div>
</section>

</body>
</html>
```